Company business card

We need a new business card design. We are IT company which is specialized for outsourcing of operations hardware and software (specially Velbrandt, we are a partner), developing custom applications and web applications, BPM solutions, auditing hw and sw. actually design was attached. But we need completely NEW.

Industry/Entity Type

Business

```html
<!DOCTYPE html>
<html lang="sk">
<head>
<meta charset="utf-8">
<title>KORVAN business card</title>
<link rel="stylesheet" href="https://fonts.googleapis.com/css2?family=Montserrat:wght@400;600;700;800&display=swap">
<style>
  :root {
    --bg: #e6e6e8;
    --brand-blue: #2b5aa8;
    --brand-blue-dark: #1f4690;
    --brand-blue-light: #3d6fbf;
    --paper: #ffffff;
    --divider: #eceef2;
    --shadow: rgba(0, 0, 0, 0.18);
  }
  html, body {
    margin: 0;
    padding: 0;
    width: 1200px;
    height: 1200px;
    overflow: hidden;
    background: var(--bg);
    font-family: "Montserrat", sans-serif;
  }
  .canvas {
    position: relative;
    width: 1200px;
    height: 1200px;
  }
  .card {
    position: absolute;
    left: 280px;
    width: 640px;
    height: 366px;
    border-radius: 22px;
    overflow: hidden;
    box-shadow: 0 10px 26px var(--shadow);
  }
  /* Front side */
  .card--front {
    top: 150px;
    background: var(--brand-blue);
  }
  .front-pattern {
    position: absolute;
    inset: 0;
    background: linear-gradient(160deg, var(--brand-blue-light) 0%, var(--brand-blue) 50%, var(--brand-blue-dark) 100%);
  }
  .front-brand {
    position: absolute;
    inset: 0;
    display: flex;
    align-items: center;
    justify-content: center;
    gap: 22px;
  }
  .brand-square {
    width: 120px;
    height: 120px;
    background: var(--paper);
    flex: none;
  }
  .front-brand .brand-name {
    color: var(--paper);
    font-weight: 800;
    font-size: 68px;
    letter-spacing: 1px;
  }
  /* Back side */
  .card--back {
    top: 620px;
    background: var(--paper);
  }
  .back-divider {
    position: absolute;
    left: 300px;
    top: 0;
    bottom: 0;
    width: 2px;
    background: var(--divider);
  }
  .back-brand {
    position: absolute;
    left: 36px;
    top: 142px;
    width: 250px;
    display: flex;
    align-items: center;
    gap: 12px;
  }
  .back-brand .brand-square {
    width: 82px;
    height: 82px;
    background: var(--brand-blue);
  }
  .back-brand__text {
    display: flex;
    flex-direction: column;
    color: var(--brand-blue);
    font-weight: 800;
    line-height: 1;
  }
  .back-brand .brand-name {
    font-size: 31px;
  }
  .back-brand .brand-suffix {
    margin-top: 6px;
    font-size: 18px;
  }
  .contact {
    position: absolute;
    left: 340px;
    top: 58px;
    width: 280px;
    color: var(--brand-blue);
  }
  .contact__name {
    margin: 0;
    font-size: 25px;
    font-weight: 700;
    white-space: nowrap;
  }
  .contact__role {
    margin: 8px 0 26px 20px;
    font-size: 12px;
    font-weight: 400;
  }
  .contact__list {
    list-style: none;
    margin: 0;
    padding: 0;
    font-size: 13px;
    line-height: 22px;
  }
  .contact__list li {
    display: flex;
    align-items: center;
    gap: 10px;
    white-space: nowrap;
  }
  .contact__icon {
    width: 14px;
    height: 14px;
    flex: none;
  }
  .contact__list .no-icon { padding-left: 24px; }
  .web-band {
    position: absolute;
    right: 0;
    bottom: 0;
    width: 300px;
    height: 70px;
  }
  .web-band svg { position: absolute; inset: 0; width: 100%; height: 100%; }
  .web-band__url {
    position: absolute;
    right: 36px;
    bottom: 22px;
    color: var(--paper);
    font-size: 14px;
    font-weight: 400;
  }
</style>
</head>
<body>
<main class="canvas">

  <section class="card card--front">
    <div class="front-pattern" role="img" aria-label="Faint repeating pattern of brand digits over blue gradient"></div>
    <div class="front-brand">
      <div class="brand-square"></div>
      <span class="brand-name">KORVAN</span>
    </div>
  </section>

  <section class="card card--back">
    <div class="back-divider"></div>
    <div class="back-brand">
      <div class="brand-square"></div>
      <div class="back-brand__text">
        <span class="brand-name">KORVAN</span>
        <span class="brand-suffix">s.r.o.</span>
      </div>
    </div>

    <div class="contact">
      <h1 class="contact__name">Marek Dolinský</h1>
      <p class="contact__role">CEO</p>
      <ul class="contact__list">
        <li class="no-icon">+421 (0) 900 555 014</li>
        <li>
          <svg class="contact__icon" viewBox="0 0 16 16" aria-hidden="true">
            <path d="M3 2h3l1 3-2 1a8 8 0 0 0 4 4l1-2 3 1v3c0 1-1 2-2 2A11 11 0 0 1 1 4c0-1 1-2 2-2z" fill="var(--brand-blue)"/>
          </svg>
          marek.dolinsky@korvan.sk
        </li>
        <li>
          <svg class="contact__icon" viewBox="0 0 16 16" aria-hidden="true">
            <rect x="1" y="3" width="14" height="10" fill="var(--brand-blue)"/>
            <path d="M1 3l7 6 7-6" fill="none" stroke="#fff" stroke-width="1.4"/>
          </svg>
          Lipová 12 811 01 Bratislava
        </li>
      </ul>
    </div>

    <div class="web-band">
      <svg viewBox="0 0 300 70" preserveAspectRatio="none" aria-hidden="true">
        <polygon points="0,0 300,0 300,70 8,70" fill="var(--brand-blue)"/>
      </svg>
      <span class="web-band__url">www.korvan.sk</span>
    </div>
  </section>

</main>
</body>
</html>
```